Mobile App UI Redesign for Service Booking app

Bookora is a business management system made especially for service based businesses (our subscribers). It enables systemising your service businesses. This can be used by diverse industries like automotive service, beauty (hair salons, nail spas), Spas, Chiropractor, acupuntcure, osteo, yoga studio, business coach, etc.

One component of this management system is a consumer app that the users (customers of our subscribers) can use to book in services with businesses (subscribers). Any business that provides services, either 1-to-1(personal training/ hair cut, etc) or 1-to-many (classes/ sessions)can get their users to download the app and book straight away in real time.

The current app is built as a version that is available to all subscribers. Hence the search screen at the beginning of the app. Our subscribers have the option to brand this app, with their own logo and colours.

The UI of the app needs to be designed using flat and clean UI design trends that are currently prevailing for B2C apps. Even the sliding menu panel can be removed and alternative placement of this functionality can be suggested. The color palette used for the design should be limited (3-5 colours) so that minimum effort is required to convert this into our customers branded app.

The Current UI screens are open to suggestions for change. For ease of booking in minimum steps, consolidation of functionality on different screens can be suggested, accompanies by a rational reason with the objective of having a simple and straight forward user experience.

User should be able to move from one function to another (booking > view appointments > profile) in no more than 1 or max 2 gestures.

Target Market(s)

Service Based Businesses that require customers to book in services or sessions with them. These can include health services (chiro, physio, osteo, accupuncture, etc) Beauty (hair salon, nail spa, health spa, etc) automotive service (car service, motorcycle service, bike service, etc)

Industry/Entity Type

Business

Requirements
Must have
• Design files to be delivered in JPG and Vectored PSD format

```html
<!DOCTYPE html>
<html lang="en">
<head>
<meta charset="utf-8">
<title>Bookora – App Screens</title>
<link href="https://fonts.googleapis.com/css2?family=Open+Sans:wght@400;600;700&display=swap" rel="stylesheet">
<style>
:root{
  --brand:#a3195b;
  --brand-soft:#c9588c;
  --ink:#222;
  --muted:#777;
  --line:#d9d9d9;
  --chip:#ececec;
  --tile:#e6e1e4;
  --page:#f2f2f2;
  --white:#fff;
}
*{box-sizing:border-box;margin:0;padding:0}
html,body{width:699px;height:1200px;overflow:hidden;background:var(--page);font-family:"Open Sans",Arial,sans-serif;color:var(--ink)}
.screen{position:absolute;width:333px;height:582px;background:var(--white);overflow:hidden;box-shadow:0 0 0 1px #ddd}
.s1{left:12px;top:12px}.s2{left:354px;top:12px}.s3{left:12px;top:606px}.s4{left:354px;top:606px}
.hero{position:absolute;left:0;top:0;width:100%;background:linear-gradient(160deg,#c2406e 0%,#d9607a 35%,#9a3a7a 70%,#6a2a70 100%)}
.bar{position:absolute;left:0;top:0;width:100%;height:62px;background:var(--brand)}
.status{position:absolute;left:0;top:0;width:100%;height:20px;color:#fff;font-size:9px;display:flex;justify-content:space-between;align-items:center;padding:0 8px}
.nav{position:absolute;left:0;top:22px;width:100%;height:38px;display:flex;align-items:center;justify-content:center;color:#fff;font-size:15px;font-weight:600}
.nav .back{position:absolute;left:10px;top:8px}
.nav .action{position:absolute;right:12px;top:8px}
.intro{position:absolute;left:22px;right:22px;top:70px;color:#fff;font-size:11.5px;line-height:1.45;text-align:center}
.divider-label{position:absolute;left:22px;right:22px;top:170px;display:flex;align-items:center;gap:10px;font-size:11.5px;color:#555}
.divider-label::before,.divider-label::after{content:"";flex:1;height:1px;background:var(--line)}
.field{position:absolute;left:52px;width:230px;height:42px;border:1px solid #c8c8c8;border-radius:4px;display:flex;align-items:center;justify-content:center;color:#999;font-size:12px}
.field .caret{position:absolute;right:12px;top:16px;font-size:8px;color:#666}
.btn{position:absolute;background:var(--brand);color:#fff;font-size:14px;display:flex;align-items:center;justify-content:center;border-radius:3px}
.results-band{position:absolute;left:0;top:62px;width:100%;height:22px;background:var(--brand-soft);color:#fff;font-size:10px;display:flex;align-items:center;justify-content:center}
.result{position:absolute;left:0;width:100%;height:100px;border-bottom:1px solid var(--line)}
.tile{position:absolute;display:flex;align-items:center;justify-content:center;font-weight:600;color:var(--brand);background:var(--tile)}
.result .tile{left:10px;top:12px;width:76px;height:76px;font-size:13px}
.result h3{position:absolute;left:98px;top:18px;font-size:13px;font-weight:700}
.addr{font-size:10.5px;color:var(--muted);line-height:1.35}
.result .addr{position:absolute;left:98px;top:37px}
.phone{display:flex;align-items:center;gap:6px;font-size:11px;color:var(--brand)}
.result .phone{position:absolute;left:98px;top:70px}
.split{position:absolute;display:flex;background:var(--chip);font-size:12.5px;color:#555}
.split span{flex:1;display:flex;align-items:center;justify-content:center}
.lorem{position:absolute;font-size:10.5px;line-height:1.5;color:#444}
</style>
</head>
<body>

<section class="screen s1">
  <div class="hero" style="height:152px" role="img" aria-label="Soft pink and purple header backdrop"></div>
  <div class="status"><span>●●●●○ Carrier</span><span>7:26 PM</span><span>100%</span></div>
  <div class="nav">
    <svg class="back" width="22" height="22" viewBox="0 0 22 22"><circle cx="11" cy="11" r="10" fill="none" stroke="#fff" stroke-width="1.5"/><path d="M13 6l-5 5 5 5" fill="none" stroke="#fff" stroke-width="1.8"/></svg>
    Search a Business
  </div>
  <p class="intro">Search here for businesses that are trialling Bookora App to provide you with the convenience of booking their services on your mobile.</p>
  <div class="divider-label">Search business by</div>
  <div class="field" style="top:212px">name</div>
  <div class="field" style="top:266px">type<span class="caret">▼</span></div>
  <div class="field" style="top:320px">city<span class="caret">▼</span></div>
  <div class="field" style="top:374px">postal code</div>
  <div class="btn" style="left:42px;top:440px;width:250px;height:44px">REGISTER</div>
</section>

<section class="screen s2">
  <div class="bar"></div>
  <div class="status"><span>●●●●○ Carrier</span><span>7:26 PM</span><span>100%</span></div>
  <div class="nav">
    <svg class="back" width="22" height="22" viewBox="0 0 22 22"><circle cx="11" cy="11" r="10" fill="none" stroke="#fff" stroke-width="1.5"/><path d="M13 6l-5 5 5 5" fill="none" stroke="#fff" stroke-width="1.8"/></svg>
    Search Results
    <svg class="action" width="22" height="22" viewBox="0 0 22 22"><circle cx="11" cy="11" r="10" fill="none" stroke="#fff" stroke-width="1.5"/><path d="M6 7h10l-4 5v4l-2 1v-5z" fill="#fff"/></svg>
  </div>
  <div class="results-band">4 results of "Something"</div>

  <article class="result" style="top:84px">
    <div class="tile">Alto</div>
    <h3>Something Awesome</h3>
    <p class="addr">Maple Street, Birch Heights<br>CDO 9000</p>
    <p class="phone"><svg width="11" height="11" viewBox="0 0 24 24"><path d="M6.6 10.8a15 15 0 006.6 6.6l2.2-2.2a1 1 0 011-.25 11.4 11.4 0 003.6.57 1 1 0 011 1V20a1 1 0 01-1 1A17 17 0 013 4a1 1 0 011-1h3.5a1 1 0 011 1c0 1.25.2 2.45.57 3.57a1 1 0 01-.25 1z" fill="#555"/></svg>(088) 555-0134</p>
  </article>
  <article class="result" style="top:184px">
    <div class="tile">Fern</div>
    <h3>Something Cool</h3>
    <p class="addr">Oak Street, Pine &amp; Cedar<br>CDO 9000</p>
    <p class="phone"><svg width="11" height="11" viewBox="0 0 24 24"><path d="M6.6 10.8a15 15 0 006.6 6.6l2.2-2.2a1 1 0 011-.25 11.4 11.4 0 003.6.57 1 1 0 011 1V20a1 1 0 01-1 1A17 17 0 013 4a1 1 0 011-1h3.5a1 1 0 011 1c0 1.25.2 2.45.57 3.57a1 1 0 01-.25 1z" fill="#555"/></svg>(088) 555-0100</p>
  </article>
  <article class="result" style="top:284px">
    <div class="tile">Kite</div>
    <h3>Something New</h3>
    <p class="addr">Maple Street, Birch Heights<br>CDO 9000</p>
    <p class="phone"><svg width="11" height="11" viewBox="0 0 24 24"><path d="M6.6 10.8a15 15 0 006.6 6.6l2.2-2.2a1 1 0 011-.25 11.4 11.4 0 003.6.57 1 1 0 011 1V20a1 1 0 01-1 1A17 17 0 013 4a1 1 0 011-1h3.5a1 1 0 011 1c0 1.25.2 2.45.57 3.57a1 1 0 01-.25 1z" fill="#555"/></svg>(088) 555-0172</p>
  </article>
  <article class="result" style="top:384px">
    <div class="tile">Wren</div>
    <h3>Something Weird</h3>
    <p class="addr">Oak Street, Pine &amp; Cedar<br>CDO 9000</p>
    <p class="phone"><svg width="11" height="11" viewBox="0 0 24 24"><path d="M6.6 10.8a15 15 0 006.6 6.6l2.2-2.2a1 1 0 011-.25 11.4 11.4 0 003.6.57 1 1 0 011 1V20a1 1 0 01-1 1A17 17 0 013 4a1 1 0 011-1h3.5a1 1 0 011 1c0 1.25.2 2.45.57 3.57a1 1 0 01-.25 1z" fill="#555"/></svg>(088) 555-0128</p>
  </article>
</section>

<section class="screen s3">
  <div class="hero" style="height:192px" role="img" aria-label="Soft pink and purple header backdrop"></div>
  <div class="status"><span>●●●●○ Carrier</span><span>7:26 PM</span><span>100%</span></div>
  <div class="nav">
    <svg class="back" width="22" height="22" viewBox="0 0 22 22"><circle cx="11" cy="11" r="10" fill="none" stroke="#fff" stroke-width="1.5"/><path d="M13 6l-5 5 5 5" fill="none" stroke="#fff" stroke-width="1.8"/></svg>
    Something Weird
    <svg class="action" width="24" height="22" viewBox="0 0 24 22"><path d="M12 21l-1.5-1.3C5 15 1.5 11.8 1.5 7.8 1.5 4.5 4 2 7.2 2c1.8 0 3.6.9 4.8 2.3C13.2 2.9 15 2 16.8 2 20 2 22.5 4.5 22.5 7.8c0 4-3.5 7.2-9 11.9z" fill="#fff"/></svg>
  </div>
  <div class="tile" style="left:22px;top:80px;width:62px;height:62px;font-size:12px">Wren</div>
  <p class="addr" style="position:absolute;left:98px;top:88px;color:#fff">Oak Street, Pine &amp; Cedar<br>CDO 9000</p>
  <p class="phone" style="position:absolute;left:98px;top:124px;color:#fff"><svg width="11" height="11" viewBox="0 0 24 24"><path d="M6.6 10.8a15 15 0 006.6 6.6l2.2-2.2a1 1 0 011-.25 11.4 11.4 0 003.6.57 1 1 0 011 1V20a1 1 0 01-1 1A17 17 0 013 4a1 1 0 011-1h3.5a1 1 0 011 1c0 1.25.2 2.45.57 3.57a1 1 0 01-.25 1z" fill="#fff"/></svg>(088) 555-0128</p>
  <div class="split" style="left:14px;top:206px;width:305px;height:40px">
    <span style="border-right:1px solid #cfcfcf">Call</span><span>Message</span>
  </div>
  <p class="lorem" style="left:34px;right:34px;top:292px">Lorem ipsum dolor sit amet, consectetur adipiscing elit. Vestibulum dolor elit, mattis non quam sed, sodales vestibulum justo. Cras sed accumsan mi, in auctor nisi. Aenean mattis justo molestie, hendrerit velit eget, auctor est.</p>
  <div class="btn" style="left:42px;top:440px;width:250px;height:44px">Select Business</div>
</section>

<section class="screen s4">
  <div class="bar"></div>
  <div class="status"><span>●●●●○ Carrier</span><span>7:26 PM</span><span>100%</span></div>
  <div class="nav">
    <svg class="back" width="22" height="22" viewBox="0 0 22 22"><circle cx="11" cy="11" r="10" fill="none" stroke="#fff" stroke-width="1.5"/><path d="M13 6l-5 5 5 5" fill="none" stroke="#fff" stroke-width="1.8"/></svg>
    Something Weird
  </div>
  <div class="tile" style="left:119px;top:76px;width:95px;height:95px;font-size:16px">Wren</div>
  <h3 style="position:absolute;left:0;width:100%;top:182px;text-align:center;font-size:13px;font-weight:700">Something Weird</h3>
  <p class="addr" style="position:absolute;left:0;width:100%;top:200px;text-align:center">Oak Street, Pine &amp; Cedar<br>CDO 9000</p>
  <p class="phone" style="position:absolute;left:0;width:100%;top:234px;justify-content:center"><svg width="11" height="11" viewBox="0 0 24 24"><path d="M6.6 10.8a15 15 0 006.6 6.6l2.2-2.2a1 1 0 011-.25 11.4 11.4 0 003.6.57 1 1 0 011 1V20a1 1 0 01-1 1A17 17 0 013 4a1 1 0 011-1h3.5a1 1 0 011 1c0 1.25.2 2.45.57 3.57a1 1 0 01-.25 1z" fill="#555"/></svg>(088) 555-0128</p>
  <div class="split" style="left:14px;top:266px;width:305px;height:34px;border-radius:17px">
    <span>Call</span><span style="flex:0 0 60px"></span><span>Message</span>
  </div>
  <svg style="position:absolute;left:144px;top:260px" width="46" height="46" viewBox="0 0 46 46"><circle cx="23" cy="23" r="22" fill="#fff" stroke="#ddd"/><path d="M23 33l-1.4-1.2C16.5 27.3 13 24.3 13 20.6 13 17.6 15.4 15.2 18.4 15.2c1.7 0 3.3.8 4.6 2 1.3-1.2 2.9-2 4.6-2 3 0 5.4 2.4 5.4 5.4 0 3.7-3.5 6.7-8.6 11.2z" fill="var(--brand)"/></svg>
  <p class="lorem" style="left:34px;right:34px;top:330px">Lorem ipsum dolor sit amet, consectetur adipiscing elit. Vestibulum dolor elit, mattis non quam sed, sodales vestibulum justo. Cras sed accumsan mi, in auctor nisi. Aenean mattis justo molestie, hendrerit velit eget, auctor est.</p>
  <div style="position:absolute;left:0;top:505px;width:100%;height:1px;background:var(--line)"></div>
  <div class="btn" style="left:42px;top:520px;width:250px;height:44px">Select Business</div>
</section>

</body>
</html>
```